Steel Company / Iron Railing Business Card Template

We are a custom steel fabrication company located in Trainer, PA. In business since 1979, we recently developed a new logo, and we're looking for a business card design to help display the new logo and our business. The name of the company is Kelbrook Forge Co.. The Office Phone number is (555) 555-0143. We fabricate and install custom "wrought iron" railings on our residential side, we also fabricate and erect structural steel (think cranes and steel beams in buildings) on our commercial side. Looking to get a business card template designed. Something modern, but professional. Clear and easy to read. Front should have all business and employee information including phone number(s), email address, business information, etc. back should spotlight logo.

Industry/Entity Type

Construction / Home Improvement

Contact Information for Business Card

Business information is Kelbrook Forge Co., 48 Dunmore Ave Suite 3305, Harlow Bend, Eastshire 19074. Phone number is (555) 555-0143. Website is www.kelbrookforge.example Business card should be for "Tom Pelling" with the job title "Sales & Estimating" but be editable for other employees. Tom's phone number is (610) 555-0178

Colors

Designer to choose colors to be used in the design.

Requirements
Must have
• Modern Feel, Design should be sized for standard business card sizing 3.5" x 2" (88.9mm x 50.8mm)

```html
<!DOCTYPE html>
<html lang="en">
<head>
<meta charset="utf-8">
<title>Kelbrook Forge Co. — Business Card</title>
<link rel="stylesheet" href="https://fonts.googleapis.com/css2?family=Alfa+Slab+One&family=Montserrat:wght@400;500;700&display=swap">
<style>
  :root {
    --bg: #1c1c1c;
    --card-black: #0d0d0d;
    --card-white: #ffffff;
    --brand-blue: #24408e;
    --brand-red: #d42027;
    --ink: #2a2a2a;
    --emboss: #9a9a9a;
  }
  * { box-sizing: border-box; margin: 0; padding: 0; }
  html, body { width: 1200px; height: 900px; overflow: hidden; }
  body {
    background: var(--bg);
    font-family: "Montserrat", sans-serif;
    position: relative;
  }
  .card {
    position: absolute;
    width: 560px;
    height: 320px;
    overflow: hidden;
    box-shadow: 0 14px 30px rgba(0,0,0,.55);
  }

  /* Back of card */
  .card-back {
    left: 70px; top: 80px;
    background: var(--card-black);
    display: flex; align-items: center; justify-content: center;
  }
  .back-mark { display: flex; align-items: center; gap: 18px; }
  .back-mark .dot {
    width: 46px; height: 46px; border-radius: 50%;
    background: var(--brand-red);
  }
  .back-mark .wordmark {
    font-weight: 700; font-size: 34px; color: var(--emboss);
    letter-spacing: .5px;
  }

  /* Front of card */
  .card-front {
    left: 570px; top: 500px;
    background: var(--card-white);
  }
  .front-mark {
    position: absolute; left: 28px; top: 100px;
    width: 222px;
    display: flex; align-items: center; gap: 12px;
  }
  .front-mark .dot {
    flex: none; width: 34px; height: 34px; border-radius: 50%;
    background: var(--brand-red);
  }
  .front-mark .wordmark {
    font-weight: 700; font-size: 27px; line-height: 1.12;
    color: var(--brand-blue);
  }
  .divider {
    position: absolute; left: 256px; top: 40px;
    width: 2px; height: 198px; background: var(--brand-red);
  }
  .details { position: absolute; left: 274px; top: 38px; right: 12px; }
  .employee-name {
    font-family: "Alfa Slab One", serif; font-size: 25px; font-weight: 400;
    color: var(--brand-blue); line-height: 1; letter-spacing: .3px;
  }
  .employee-title {
    font-size: 16px; color: var(--brand-red); font-weight: 500;
    margin-top: 4px;
  }
  .address {
    font-size: 14.5px; color: var(--ink); line-height: 1.35;
    margin-top: 10px;
  }
  .contact-list { list-style: none; margin-top: 10px; }
  .contact-list li {
    display: flex; align-items: center; gap: 8px;
    font-size: 14.5px; color: var(--ink); line-height: 1.55;
    white-space: nowrap;
  }
  .contact-list svg { width: 14px; height: 14px; flex: none; fill: var(--brand-blue); }
  .bottom-band { position: absolute; left: 0; bottom: 0; width: 560px; height: 26px; }
</style>
</head>
<body>

  <section class="card card-back" aria-label="Card back">
    <div class="back-mark">
      <span class="dot"></span>
      <span class="wordmark">Kelbrook Forge Co.</span>
    </div>
  </section>

  <section class="card card-front" aria-label="Card front">
    <div class="front-mark">
      <span class="dot"></span>
      <span class="wordmark">Kelbrook Forge Co.</span>
    </div>

    <div class="divider"></div>

    <div class="details">
      <h1 class="employee-name">TOM PELLING</h1>
      <p class="employee-title">Sales &amp; Estimating</p>
      <p class="address">48 Dunmore Ave Suite 3305,<br>Harlow Bend, Eastshire 19074</p>
      <ul class="contact-list">
        <li>
          <svg viewBox="0 0 24 24" aria-hidden="true"><path d="M6.6 10.8a15.1 15.1 0 0 0 6.6 6.6l2.2-2.2a1 1 0 0 1 1-.25 11.4 11.4 0 0 0 3.6.57 1 1 0 0 1 1 1V20a1 1 0 0 1-1 1A17 17 0 0 1 3 4a1 1 0 0 1 1-1h3.5a1 1 0 0 1 1 1c0 1.25.2 2.45.57 3.6a1 1 0 0 1-.25 1z"/></svg>
          (555) 555-0143
        </li>
        <li>
          <svg viewBox="0 0 24 24" aria-hidden="true"><path d="M2 5h20v14H2z M3 6l9 7 9-7" fill="none" stroke="#24408e" stroke-width="2"/></svg>
          info@kelbrookforge.example
        </li>
        <li>
          <svg viewBox="0 0 24 24" aria-hidden="true"><circle cx="12" cy="12" r="10"/><path d="M2 12h20M12 2c3 3 3 17 0 20M12 2c-3 3-3 17 0 20" fill="none" stroke="#fff" stroke-width="1.5"/></svg>
          www.kelbrookforge.example
        </li>
      </ul>
    </div>

    <svg class="bottom-band" viewBox="0 0 560 26" aria-hidden="true">
      <polygon points="0,0 362,0 356,26 0,26" fill="var(--brand-blue)"/>
      <polygon points="364,0 560,0 560,26 358,26" fill="var(--brand-red)"/>
    </svg>
  </section>

</body>
</html>
```